We are looking for Facebook and Instagram templates. To use both platforms we will use square images. We need a template for our posts, not the header image.
Most posts contain multiple images and we need a designoverlay in which we can embed our images.
Attached a screenshot of our website www.velutra.be, our logo in svg and ai. The monkey is our mascotte (excact this monkey, not another).
We offer teambuildings, the style should be fun. Colors are antracite, limegreen and white. I did attache the current layout for posts but we are not happy with this.
If we could have some small design elements (like stickers) we can always create a new layout but is feels the same.
Our website is quite simple, this should also be in these post designs. Simple forms, rounded corners.
Updates

Allow more time for the designers, good work requires more time

Target Market(s)

Teambuilding

Industry/Entity Type

Teambuilding

Other font styles liked:
• RobotoSlab

Requirements
Must have
• If we could have some small design elements (like stickers) we can always create a new layout but is feels the same.
Should not have
• Complex design, simple images works best for us

```html
<!DOCTYPE html>
<html lang="en">
<head>
<meta charset="utf-8">
<title>Velutra social post templates</title>
<link rel="stylesheet" href="https://fonts.googleapis.com/css2?family=Roboto+Slab:wght@700;800&family=Raleway:wght@400;500&family=Poppins:wght@400&display=swap">
<style>
  :root {
    --board: #8aa800;
    --lime: #aecb10;
    --antracite: #474747;
    --white: #ffffff;
    --orange: #f26b3a;
    --gold: #f3b72c;
    --photo-warm-a: #c9563f;
    --photo-warm-b: #e4b24a;
    --photo-cool-a: #5a3fd1;
    --photo-cool-b: #b2232a;
    --photo-dark-a: #1d3a1c;
    --photo-dark-b: #7a1d20;
    --photo-park-a: #5d7d3c;
    --photo-park-b: #9b2530;
  }
  * { margin: 0; padding: 0; box-sizing: border-box; }
  html, body { width: 1200px; height: 1050px; overflow: hidden; }
  body { background: var(--board); position: relative; font-family: "Raleway", sans-serif; }
  .post { position: absolute; width: 398px; height: 398px; background: var(--white); overflow: visible; }
  .post svg { display: block; overflow: visible; }
  .post--inzet { left: 185px; top: 57px; }
  .post--memories { left: 618px; top: 57px; }
  .post--teambuilding { left: 185px; top: 470px; }
  .post--stronger { left: 618px; top: 470px; }
  .slab { font-family: "Roboto Slab", serif; font-weight: 800; fill: var(--antracite); }
  .sans { font-family: "Raleway", sans-serif; fill: var(--antracite); }
  .brand { font-family: "Roboto Slab", serif; font-weight: 700; fill: var(--antracite); letter-spacing: 1.5px; }
  .sticker { stroke: var(--white); stroke-width: 3; }
  .note {
    position: absolute; left: 185px; top: 890px;
    font-family: "Poppins", sans-serif; font-size: 28.5px; line-height: 34px;
    color: var(--white);
  }
</style>
</head>
<body>
<svg width="0" height="0" style="position:absolute">
  <defs>
    <linearGradient id="warm" x1="0" y1="0" x2="1" y2="1"><stop offset="0" stop-color="var(--photo-warm-a)"/><stop offset="1" stop-color="var(--photo-warm-b)"/></linearGradient>
    <linearGradient id="cool" x1="0" y1="0" x2="1" y2="0"><stop offset="0" stop-color="var(--photo-cool-a)"/><stop offset=".55" stop-color="var(--photo-cool-b)"/><stop offset="1" stop-color="#e9e9ef"/></linearGradient>
    <linearGradient id="dark" x1="0" y1="0" x2="1" y2="1"><stop offset="0" stop-color="var(--photo-dark-b)"/><stop offset=".5" stop-color="var(--photo-dark-a)"/><stop offset="1" stop-color="#0f1a10"/></linearGradient>
    <linearGradient id="park" x1="0" y1="0" x2="1" y2="1"><stop offset="0" stop-color="var(--photo-park-a)"/><stop offset="1" stop-color="var(--photo-park-b)"/></linearGradient>
  </defs>
</svg>

<!-- Post: Inzet bouwverlof -->
<div class="post post--inzet">
  <svg width="398" height="398" viewBox="0 0 398 398">
    <path d="M213 0H398V107H273a60 60 0 0 1-60-60z" fill="var(--lime)"/>
    <path d="M0 123H167a50 50 0 0 1 50 50V398H0z" fill="var(--lime)"/>
    <text class="brand" x="329" y="34" font-size="15" text-anchor="middle">VELUTRA</text>
    <text class="brand" x="329" y="49" font-size="10" text-anchor="middle">HET FORT</text>
    <rect x="29" y="41" width="117" height="122" rx="40" fill="var(--antracite)" role="img" aria-label="Mascot monkey silhouette"/>
    <text class="slab" x="19" y="207" font-size="21">INZET</text>
    <text class="slab" x="19" y="232" font-size="21">BOUWVERLOF</text>
    <text class="sans" x="19" y="252" font-size="13">Full house met de inzet</text>
    <text class="sans" x="19" y="268" font-size="13">van de zomervakantie</text>
    <line x1="19" y1="280" x2="168" y2="280" stroke="var(--antracite)" stroke-width="1"/>
    <g class="sans" font-size="8.4">
      <text x="19" y="301">Lorem ipsum dolor sit amet, consec-</text>
      <text x="19" y="311.7">tetuer adipiscing elit, sed diam</text>
      <text x="19" y="322.4">nonummy nibh euismod tincidunt ut</text>
      <text x="19" y="333.1">laoreet dolore magna aliquam erat</text>
      <text x="19" y="343.8">volutpat. Ut wisi enim ad minim</text>
      <text x="19" y="354.5">veniam, quis nostrud exerci tation</text>
      <text x="19" y="365.2">ullamcorper suscipit lobortis nis</text>
    </g>
    <rect x="186" y="152" width="192" height="105" rx="23" fill="url(#warm)" role="img" aria-label="Photo: team solving a puzzle on the floor of a colourful room"/>
    <rect x="186" y="267" width="192" height="107" rx="23" fill="url(#cool)" role="img" aria-label="Photo: players pressing buttons on a red game wall"/>
    <circle class="sticker" cx="201" cy="152" r="17" fill="var(--orange)" role="img" aria-label="Basketball sticker"/>
    <rect class="sticker" x="345" y="335" width="36" height="48" rx="12" fill="var(--gold)" role="img" aria-label="Trophy sticker"/>
  </svg>
</div>

<!-- Post: Memories together -->
<div class="post post--memories">
  <svg width="398" height="398" viewBox="0 0 398 398">
    <path d="M0 0H236V58a50 50 0 0 1-50 50H0z" fill="var(--lime)"/>
    <path d="M364 242H398V398H314V292a50 50 0 0 1 50-50z" fill="var(--lime)"/>
    <text class="slab" x="22" y="60" font-size="30">MEMORIES</text>
    <text class="sans" x="22" y="83" font-size="22" fill="var(--white)" style="fill:var(--white)">TOGETHER</text>
    <text class="brand" x="328" y="35" font-size="15" text-anchor="middle">VELUTRA</text>
    <text class="brand" x="328" y="50" font-size="10" text-anchor="middle">HET FORT</text>
    <rect x="80" y="100" width="238" height="132" rx="23" fill="url(#warm)" role="img" aria-label="Photo: team solving a puzzle on the floor of a colourful room"/>
    <rect x="80" y="243" width="238" height="132" rx="23" fill="url(#cool)" role="img" aria-label="Photo: players pressing buttons on a red game wall"/>
    <rect class="sticker" x="266" y="78" width="70" height="58" rx="24" fill="var(--orange)" role="img" aria-label="Bucket hat sticker"/>
    <circle class="sticker" cx="85" cy="357" r="22" fill="var(--orange)" role="img" aria-label="Basketball sticker"/>
  </svg>
</div>

<!-- Post: Team building day -->
<div class="post post--teambuilding">
  <svg width="398" height="398" viewBox="0 0 398 398">
    <rect x="0" y="216" width="398" height="182" fill="var(--lime)"/>
    <text class="slab" x="36" y="72" font-size="39">TEAM</text>
    <text class="slab" x="36" y="106" font-size="39">BUILDING DAY</text>
    <text class="brand" x="329" y="35" font-size="15" text-anchor="middle">VELUTRA</text>
    <text class="brand" x="329" y="50" font-size="10" text-anchor="middle">HET FORT</text>
    <rect x="36" y="126" width="326" height="224" rx="25" fill="url(#dark)" role="img" aria-label="Photo: players moving through a green laser maze"/>
    <circle class="sticker" cx="349" cy="128" r="21" fill="var(--orange)" role="img" aria-label="Basketball sticker"/>
    <rect class="sticker" x="28" y="304" width="80" height="72" rx="22" fill="#c8643a" role="img" aria-label="Basket of balls sticker"/>
  </svg>
</div>

<!-- Post: Stronger together -->
<div class="post post--stronger">
  <svg width="398" height="398" viewBox="0 0 398 398">
    <path d="M256 0H398V80H301a45 45 0 0 1-45-45z" fill="var(--lime)"/>
    <path d="M60 292H398V398H0V352a60 60 0 0 1 60-60z" fill="var(--lime)"/>
    <text class="slab" x="36" y="75" font-size="35">STRONGER</text>
    <text class="sans" x="36" y="104" font-size="25">TOGETHER</text>
    <circle class="sticker" cx="297" cy="81" r="22" fill="var(--orange)" role="img" aria-label="Basketball sticker"/>
    <rect x="36" y="128" width="325" height="222" rx="25" fill="url(#park)" role="img" aria-label="Photo: group in tartan kilts throwing a ball outdoors"/>
    <rect class="sticker" x="26" y="320" width="38" height="52" rx="12" fill="var(--gold)" role="img" aria-label="Trophy sticker"/>
  </svg>
</div>

<p class="note">Hi! I've designed some templates and icon stickers for you.<br>Please let me know your thoughts or suggestions.<br>Thank you! Have a nice day!</p>
</body>
</html>
```